New business logo / Business Card Design

My company provides Interim Management and consultancy, for Facilities Services. Covers any aspect of facilities management, including M&E, helpdesk, asset management, supplier relationships, catering, cleaning etc. Company provides innovative solutions to exceed client needs, drawing on years of experience. Initial thoughts on logo are attached below. Fits with RAG status on projects, red, amber and green, with logo design colours around moving services from amber to green.

Target Market(s)

Facilities Management clients and service providers

Industry/Entity Type

Business

Contact Information for Business Card

Company Name = k7Rventures Ltd My name on card = Derek Whitcombe, Director Mobile = 07516309842 Email = Derek@k7rventuresltd.co.uk Twitter = @k7Rventures Ltd

Font styles to use
Sans Serif

Colors
f37122
00a990

Requirements
Must have
• Logo to be evident, with some background image in reference to Facilities Management

```html
<!DOCTYPE html>
<html lang="en">
<head>
<meta charset="utf-8">
<title>k7Rventures Ltd — Business Card</title>
<link rel="stylesheet" href="https://fonts.googleapis.com/css2?family=Arimo:wght@400&family=Bodoni+Moda:wght@500&family=Montserrat:wght@800&display=swap">
<style>
  :root {
    --page: #e6e6e6;
    --card-white: #ffffff;
    --card-black: #000000;
    --brand-orange: #ff6a00;
    --brand-green: #0f6b1a;
    --ink: #111111;
    --text-light: #ffffff;
  }
  * { box-sizing: border-box; margin: 0; padding: 0; }
  html, body {
    width: 1189px; height: 1200px; overflow: hidden;
    background: var(--page);
  }
  .stage {
    width: 1189px; height: 1200px;
    display: flex; align-items: center; justify-content: center;
  }
  .card {
    width: 1000px; height: 571px;
    display: flex; flex-direction: column;
    background: var(--card-black);
  }
  .card__top {
    height: 280px; background: var(--card-white);
    display: flex; align-items: center; justify-content: center;
    padding-bottom: 40px;
  }
  .brand-name {
    font-family: "Montserrat", sans-serif; font-weight: 800;
    font-size: 74px; color: var(--ink); letter-spacing: 0.5px;
  }
  .card__band { height: 22px; background: var(--brand-orange); }
  .card__bottom {
    flex: 1; position: relative; color: var(--text-light);
  }
  .person { position: absolute; left: 60px; top: 64px; width: 360px; }
  .person__name {
    font-family: "Bodoni Moda", serif; font-weight: 500;
    font-size: 39px; line-height: 1.05; color: var(--brand-green);
    white-space: nowrap;
  }
  .person__role {
    font-family: "Arimo", sans-serif; font-size: 32px; line-height: 1.15;
  }
  .divider {
    position: absolute; left: 441px; top: 56px;
    width: 3px; height: 157px; background: var(--brand-orange);
  }
  .contacts {
    position: absolute; left: 484px; top: 82px; list-style: none;
    font-family: "Arimo", sans-serif; font-size: 28px;
  }
  .contacts li { display: flex; align-items: center; height: 37px; white-space: nowrap; }
  .contacts svg { width: 22px; height: 22px; margin-right: 19px; flex: none; }
</style>
</head>
<body>
<main class="stage">
  <section class="card">
    <header class="card__top">
      <h1 class="brand-name">k7Rventures Ltd</h1>
    </header>
    <div class="card__band"></div>
    <div class="card__bottom">
      <div class="person">
        <p class="person__name">Derek Whitcombe</p>
        <p class="person__role">Director</p>
      </div>
      <div class="divider"></div>
      <ul class="contacts">
        <li>
          <svg viewBox="0 0 22 22" aria-hidden="true">
            <rect width="22" height="22" rx="2" fill="var(--brand-green)"/>
            <path d="M7 4 L10 4 L10 8 L8.5 9 Q9.5 12.5 13 13.5 L14 12 L18 12 L18 15 Q17 18 14 18 Q6 16 4 8 Q4 5 7 4 Z" fill="#000"/>
          </svg>
          <span>07516309842</span>
        </li>
        <li>
          <svg viewBox="0 0 22 22" aria-hidden="true">
            <rect y="3" width="22" height="16" rx="1" fill="var(--brand-green)"/>
            <path d="M2 6 L11 12 L20 6" fill="none" stroke="#000" stroke-width="1.6"/>
          </svg>
          <span>Derek@k7rventuresltd.co.uk</span>
        </li>
        <li>
          <svg viewBox="0 0 22 22" aria-hidden="true">
            <rect width="22" height="22" rx="2" fill="var(--brand-green)"/>
          </svg>
          <span>@k7Rventures Ltd</span>
        </li>
      </ul>
    </div>
  </section>
</main>
</body>
</html>
```